I want a double sided flyer possibly with a picture of a lawn or grass.
Company name, phone number, email, and logo
Corvane Lawn Management, (404)672-8154,Corvane_Lawn@brisknet.com
Company services
Fertilization and weed control,Lawn and Landscape maintenance, mowing, pruning, aeration, landscape and Christmas lights,

```html
<!DOCTYPE html>
<html lang="en">
<head>
<meta charset="utf-8">
<title>Corvane Lawn Management – Flyer</title>
<link href="https://fonts.googleapis.com/css2?family=PT+Sans+Narrow:wght@400;700&family=Open+Sans:wght@400;600&display=swap" rel="stylesheet">
<style>
  :root{
    --leaf:#3d9a2f;
    --leaf-deep:#2e7d24;
    --leaf-bright:#4cae3a;
    --lime:#a9cf1c;
    --sun:#f5ec1a;
    --ink:#3a3a3a;
    --paper:#ffffff;
    --rule:#cfcfcf;
  }
  *{margin:0;padding:0;box-sizing:border-box}
  html,body{width:1200px;height:900px;overflow:hidden;background:var(--paper)}
  .canvas{position:relative;width:1200px;height:900px;font-family:"PT Sans Narrow",sans-serif}

  .lawn-photo{position:absolute;background:
      linear-gradient(180deg,#ffffff 0%,#f8fbe4 35%,#d9eca0 62%,#8fcb3c 80%,#4f9f22 100%)}
  .front-photo{left:62px;top:246px;width:189px;height:371px}
  .back-photo{left:641px;top:246px;width:527px;height:329px;
    background:linear-gradient(180deg,#ffffff 0%,#f6fbe0 30%,#dcefa6 58%,#8ccb3a 78%,#4a9a20 100%)}

  .brand{position:absolute;left:62px;top:360px;width:189px;text-align:center;color:var(--leaf)}
  .brand-dot{width:44px;height:44px;border-radius:50%;background:var(--leaf);margin:0 auto 14px}
  .brand-name{font-weight:700;font-size:25px;line-height:1.05}

  .offers{position:absolute;left:256px;top:246px;width:334px;height:329px;
    background:linear-gradient(90deg,var(--leaf-bright),var(--leaf-deep))}
  .coupon{position:absolute;left:14px;width:306px;height:131px;border:1.5px dashed rgba(255,255,255,.85);
    border-radius:10px;text-align:right;padding-right:27px;color:var(--paper)}
  .coupon-one{top:26px}
  .coupon-two{top:172px}
  .coupon-amount{display:block;color:var(--sun);font-size:44px;line-height:1;margin-top:30px}
  .coupon-label{display:block;font-size:27px;line-height:1.1}

  .band{position:absolute;top:578px;height:39px;display:flex;align-items:center;white-space:nowrap}
  .tag{position:absolute;top:578px;height:39px;color:var(--paper);font-size:17px;display:flex;align-items:center;white-space:nowrap}
  .tag-quotes{left:256px;width:194px;padding-left:20px;color:#2f4d10;
    background:var(--lime);clip-path:polygon(0 0,88% 0,100% 100%,0 100%)}
  .tag-name{left:641px;width:217px;padding-left:26px;font-family:"Open Sans",sans-serif;font-size:12.5px;
    background:var(--leaf);clip-path:polygon(0 0,90% 0,100% 100%,0 100%)}
  .contact{color:var(--ink);font-size:17px;gap:6px}
  .contact svg{flex:none}
  .front-phone{left:448px}
  .back-mail{left:860px;width:176px;font-size:13.5px}
  .divider{position:absolute;left:1040px;top:586px;width:1px;height:22px;background:var(--rule)}
  .back-phone{left:1048px;font-size:16px}

  .headline{position:absolute;right:383px;top:340px;text-align:right;color:var(--ink);line-height:.92;font-weight:400}
  .headline span{display:block}
  .hl-we{font-size:33px}
  .hl-care{font-size:45px}
  .hl-for{font-size:33px}
  .hl-yard{font-size:46px;color:var(--leaf)}

  .services-bar{position:absolute;left:836px;top:328px;width:10px;height:162px;background:var(--leaf)}
  .services{position:absolute;left:846px;top:328px;width:290px;height:162px;padding:10px 0 0 20px;
    background:rgba(255,255,255,.72);clip-path:polygon(0 0,93% 0,100% 14%,100% 100%,0 100%)}
  .services-title{font-size:19px;color:var(--leaf);font-weight:400;margin-bottom:2px}
  .services-list{list-style:none;font-family:"Open Sans",sans-serif;font-size:11.3px;color:var(--ink)}
  .services-list li{height:20px;line-height:20px;position:relative;padding-left:12px}
  .services-list li::before{content:"";position:absolute;left:0;top:8px;width:5px;height:5px;border-radius:50%;background:var(--leaf-bright)}
</style>
</head>
<body>
<div class="canvas">
  <div class="lawn-photo front-photo" role="img" aria-label="Soft-focus photo of fresh green grass under bright sunlight"></div>
  <div class="brand">
    <div class="brand-dot"></div>
    <div class="brand-name">Corvane Lawn Management</div>
  </div>
  <div class="offers">
    <div class="coupon coupon-one">
      <span class="coupon-amount">$50 OFF</span>
      <span class="coupon-label">Mowing Service</span>
    </div>
    <div class="coupon coupon-two">
      <span class="coupon-amount">$50 OFF</span>
      <span class="coupon-label">Annual Lawn Service</span>
    </div>
  </div>
  <div class="tag tag-quotes">Free Quotes Available!</div>
  <div class="band contact front-phone">
    <svg width="22" height="22" viewBox="0 0 22 22" aria-hidden="true"><circle cx="11" cy="11" r="9.5" fill="none" stroke="#3d9a2f" stroke-width="2"/><path d="M7.5 6.5l2 0 1 2.5-1.3 1a6 6 0 0 0 2.8 2.8l1-1.3 2.5 1 0 2c-4.5.3-8.3-3.5-8-8z" fill="#3d9a2f"/></svg>
    <span>(404)672-8154</span>
  </div>

  <div class="lawn-photo back-photo" role="img" aria-label="Soft-focus photo of green grass with sunlit bokeh background"></div>
  <h1 class="headline">
    <span class="hl-we">WE</span>
    <span class="hl-care">CARE</span>
    <span class="hl-for">FOR YOUR</span>
    <span class="hl-yard">YARD!</span>
  </h1>
  <div class="services-bar"></div>
  <section class="services">
    <h2 class="services-title">COMPANY SERVICES</h2>
    <ul class="services-list">
      <li>Fertilization and weed control</li>
      <li>Lawn and Landscape maintenance</li>
      <li>Mowing</li>
      <li>Pruning</li>
      <li>Aeration</li>
      <li>Landscape and Christmas lights</li>
    </ul>
  </section>
  <div class="tag tag-name">Corvane Lawn Management</div>
  <div class="band contact back-mail">
    <svg width="20" height="14" viewBox="0 0 20 14" aria-hidden="true"><rect x="1" y="1" width="18" height="12" fill="none" stroke="#3d9a2f" stroke-width="1.6"/><path d="M1 1l9 7 9-7" fill="none" stroke="#3d9a2f" stroke-width="1.6"/></svg>
    <span>Corvane_Lawn@brisknet.com</span>
  </div>
  <div class="divider"></div>
  <div class="band contact back-phone">
    <svg width="22" height="22" viewBox="0 0 22 22" aria-hidden="true"><circle cx="11" cy="11" r="9.5" fill="none" stroke="#3d9a2f" stroke-width="2"/><path d="M7.5 6.5l2 0 1 2.5-1.3 1a6 6 0 0 0 2.8 2.8l1-1.3 2.5 1 0 2c-4.5.3-8.3-3.5-8-8z" fill="#3d9a2f"/></svg>
    <span>(404)672-8154</span>
  </div>
</div>
</body>
</html>
```